The Ridgeway Aerial Group Flyer to entice people to call us.

We negotiate contracts for phone masts (commercial leases). We also sell phone masts, remove phone masts, oversee the build of phone masts etc but act only for landlords. Our website is www.ridgewayaerialgroup.co.uk and i would like the flyer to reflect the branding and colour scheme on it. Ideally, i would like a tri-fold flyer. One page should be our contact details. You can use the images i have uploaded but also, you can use some of your own if you feel there are appropriate (ie people etc). We want to project the image of looking after landlords who have phone masts and making them a lot of money. I can provide the section titles and wording.

Target Market(s)

Landowners, can be big corporations like Brambos or Utility companies- or farmers and people who own buildings.

Industry/Entity Type

Telecommunications

Font styles to use
Sans Serif

Requirements
Must have
• Must have our colour scheme from our website (www.ridgewayaerialgroup.co.uk), must look modern and catchy, must have our contact details, must have pictures of one stand alone mast (tower) and one rooftop mast. Must have our logo (which should be attached).
Nice to have
• Perhaps some pictures of people looking happy, maybe an old couple, maybe a picture of a corporate individual, punchy headings.

```html
<!DOCTYPE html>
<html lang="en">
<head>
<meta charset="utf-8">
<title>The Ridgeway Aerial Group – Tri-fold Flyer</title>
<link rel="stylesheet" href="https://fonts.googleapis.com/css2?family=Open+Sans:ital,wdth,wght@0,75..100,300..800;1,75..100,300..800&family=Oswald:wght@500&display=swap">
<style>
:root{
  --green:#4b6a2f;
  --green-text:#4a6a2c;
  --ink:#6a6a6a;
  --ink-dark:#222;
  --canvas:#cbcbcb;
  --sheet:#ffffff;
  --panel-grey:#ececec;
  --sky-top:#3e6ea8;
  --sky-low:#a9c3de;
}
*{box-sizing:border-box;margin:0;padding:0}
html,body{width:772px;height:1200px;overflow:hidden;background:var(--canvas)}
body{font-family:"Open Sans",Arial,sans-serif;color:var(--ink)}
.stage{position:absolute;left:0;top:0;width:922px;height:1434px;transform:scale(0.83731);transform-origin:0 0}
.side-label{position:absolute;left:0;width:922px;text-align:center;font-style:italic;font-size:19px;color:#333}
.sheet{position:absolute;left:45px;width:847px;height:602px;background:var(--sheet);box-shadow:2px 4px 6px rgba(0,0,0,.35)}
.panel{position:absolute;top:0;height:100%}
.abs{position:absolute}
.photo{position:absolute}
.photo.sky{background:linear-gradient(180deg,var(--sky-top) 0%,#6b93c4 55%,var(--sky-low) 100%)}
.photo.ground::after{content:"";position:absolute;left:0;right:0;bottom:0;height:14%;background:linear-gradient(180deg,#5d7a3a,#3f5a28)}
.body-copy{font-size:8.3px;line-height:12px;text-align:justify;color:var(--ink)}
.body-copy p+p{margin-top:12px}
.body-copy strong{color:var(--green-text);font-weight:600}
.lead{color:var(--green-text);font-size:13.4px;line-height:15.5px;text-align:justify}
.kicker{color:var(--green-text);font-size:11px;line-height:15px;text-transform:uppercase}
.section-title{color:var(--green-text);font-size:14.5px;font-weight:400;text-transform:uppercase;letter-spacing:-.1px;white-space:nowrap}
.green-bar{position:absolute;background:var(--green);color:#fff}
.contact-bar{left:0;top:563px;width:847px;height:26px;display:flex;font-size:11px;align-items:center}
.contact-bar span{display:flex;align-items:center;gap:6px;justify-content:center}
.contact-bar svg{width:11px;height:11px}
.address{text-align:center;color:var(--green-text);font-size:11.5px;line-height:16px}
.address .name{font-weight:700;margin-bottom:4px}
.brand{position:absolute;left:20px;top:36px;display:flex;align-items:center;gap:8px;color:var(--green-text);font-weight:700;font-size:20px;line-height:22px;white-space:nowrap}
.brand .dot{width:13px;height:13px;border-radius:50%;background:var(--green);flex:none}
.tagline{font-family:"Oswald","Arial Narrow",sans-serif;font-weight:500;color:var(--green-text);font-size:27px;line-height:34px;letter-spacing:.2px}
.promo{position:absolute;display:flex}
.services{list-style:none;font-size:10px;line-height:14.4px;color:var(--ink-dark)}
.services li{display:flex;align-items:center;gap:6px}
.services svg{width:9px;height:9px;flex:none}
.cta{font-size:11px;line-height:16px}
.call-bar{display:flex;align-items:center;justify-content:center;gap:5px;font-size:10.5px;font-stretch:75%;white-space:nowrap}
.call-bar b{font-size:12.5px;font-weight:700}
</style>
</head>
<body>
<div class="stage">

  <div class="side-label" style="top:26px">outside</div>

  <section class="sheet outside" style="top:70px">
    <div class="panel" style="left:0;width:285px">
      <p class="lead abs" style="left:18px;top:20px;width:255px">The Ridgeway Aerial Group is a firm of telecoms surveyors with over 15 years’ experience of dealing with mobile phone mast operators.</p>
      <div class="photo sky ground" style="left:18px;top:93px;width:255px;height:312px" role="img" aria-label="Lattice phone mast tower against a blue sky beside a building roof"></div>
      <div class="body-copy abs" style="left:18px;top:421px;width:260px">
        <p>We have built up a massive data base of thousands of comparable mobile phone mast deals to aid us in our telecoms negotiations. All our surveyors have spent time working for phone mast operators and know the industry inside out. We now work <strong>exclusively for landlords</strong>, fighting your corner, ensuring our landlords get the highest rents and best lease terms available in the market place.</p>
        <p>Many of the original mobile phone mast leases / agreements are now coming up for renewal. This is an ideal opportunity for landlords to achieve the best deal.</p>
      </div>
    </div>

    <div class="panel" style="left:285px;width:283px;background:var(--panel-grey)">
      <p class="kicker abs" style="left:9px;top:24px;width:265px">We can help you swap your rent<br>for a large cash lump sum</p>
      <div class="photo" style="left:9px;top:70px;width:263px;height:177px;background:linear-gradient(160deg,#dfe6ec,#b8c6d3 60%,#e9e4dc)" role="img" aria-label="Smiling couple shaking hands with an adviser across a desk"></div>
      <p class="abs" style="left:12px;top:258px;width:258px;color:var(--green-text);font-size:11.5px;line-height:15px;text-align:justify">We are currently offering to review telecoms leases for free and provide landlords with our recommendations.</p>
      <div class="body-copy abs" style="left:11px;top:308px;width:262px;font-size:7.9px">
        <p>If you would like to take us up on this free no obligation offer, send a copy of your agreement and any recent correspondence to us, either via post or email using the details on this flyer. Please also provide us with your name, contact number and let us know the current rent you are achieving so we can see if there is room for improvement. Once we have received this, one of our surveyors will give you a call when convenient to talk through your lease with you, highlighting anything we feel needs addressing, any opportunity to increase the rent, or to discuss a specific issue you are having with your mast (i.e. an upgrade request).</p>
      </div>
      <div class="address abs" style="left:0;top:447px;width:283px">
        <p class="name">The Ridgeway Aerial Group Ltd</p>
        <p>The Beacon Offices,<br>Millstone Business Park,<br>Hollin Vale, Shropshire, SY99 2QT</p>
        <p style="margin-top:8px">t: 01632 960418<br>f: 01632 960419</p>
      </div>
    </div>

    <div class="panel" style="left:568px;width:279px">
      <div class="photo sky" style="left:0;top:120px;width:279px;height:351px" role="img" aria-label="Slim monopole phone mast rising above green hedgerow under a cloudy blue sky"></div>
      <svg class="abs" style="left:0;top:0" width="279" height="145" viewBox="0 0 279 145" aria-hidden="true">
        <defs><linearGradient id="brand-fade" x1="0" y1="0" x2="1" y2="0"><stop offset="0" stop-color="#fff"/><stop offset="1" stop-color="#e4e4e4"/></linearGradient></defs>
        <path d="M0 0H279V108C200 116 110 124 0 138Z" fill="url(#brand-fade)"/>
        <path d="M0 138C110 124 200 116 279 108" fill="none" stroke="var(--green)" stroke-width="4"/>
      </svg>
      <div class="brand"><span class="dot"></span><span>THE RIDGEWAY<br>AERIAL GROUP</span></div>
      <div class="tagline abs" style="left:12px;top:484px">EXCLUSIVELY<br>FOR LANDLORDS</div>
    </div>

    <div class="green-bar contact-bar">
      <span style="width:285px">
        <svg viewBox="0 0 12 12"><circle cx="6" cy="6" r="6" fill="#fff"/><rect x="3" y="4" width="6" height="4.2" fill="none" stroke="var(--green)" stroke-width=".9"/><path d="M3 4L6 6.4L9 4" fill="none" stroke="var(--green)" stroke-width=".9"/></svg>
        info@ridgewayaerialgroup.co.uk</span>
      <span style="width:283px">
        <svg viewBox="0 0 12 12"><circle cx="6" cy="6" r="5.3" fill="none" stroke="#fff" stroke-width="1.1"/><ellipse cx="6" cy="6" rx="2.3" ry="5.3" fill="none" stroke="#fff" stroke-width=".9"/><path d="M.7 6H11.3M1.8 3.4H10.2M1.8 8.6H10.2" stroke="#fff" stroke-width=".9"/></svg>
        www.ridgewayaerialgroup.co.uk</span>
      <span style="width:279px">
        <svg viewBox="0 0 12 12"><circle cx="6" cy="6" r="6" fill="#fff"/><path d="M4 2.8L5.2 4.6L4.6 5.4Q5.4 7 6.8 7.6L7.6 7L9.3 8.2L8.6 9.3Q5.8 9.4 3.6 6.3Q2.6 4.6 3 3.4Z" fill="var(--green)"/></svg>
        01632 960418</span>
    </div>
  </section>

  <div class="side-label" style="top:732px">inside</div>

  <section class="sheet inside" style="top:772px">
    <div class="panel" style="left:0;width:277px">
      <h2 class="section-title abs" style="left:11px;top:14px">Sell your phone mast</h2>
      <div class="photo sky ground" style="left:11px;top:45px;width:257px;height:193px" role="img" aria-label="Tall slim mast standing in open heathland under a blue sky"></div>
      <div class="body-copy abs" style="left:11px;top:248px;width:257px">
        <p>We can also assist landlords in selling their phone mast. We have strong links with many large investors who regularly purchase the freehold or leasehold interest of masts and will pay a cash lump sum of tens, even hundreds of thousands of pounds.This can be done in a matter of weeks and the cash is yours to spend however you like, regardless of whether the mast stays for the duration of the investors leasehold or not. We can negotiate flexible terms, such as a buyback option so please call us today to discuss.</p>
      </div>
      <h2 class="section-title abs" style="left:11px;top:377px">Getting a phone mast</h2>
      <div class="body-copy abs" style="left:11px;top:404px;width:257px">
        <p>If you don’t currently have a mast located on your land but are interested in receiving thousands of pounds a year in rental income, or you have a redundant mast you would like to market, we offer a free advertising service on our website. We will market your land to phone mast operators with a view to having a mast located there. Please visit the ‘Advertise My Site’ link on our website to take advantage of this service.</p>
      </div>
      <div class="promo" style="left:11px;top:515px;width:257px;height:66px;background:#e3e3e3">
        <div style="margin:6px;width:90px;height:54px;background:linear-gradient(135deg,#c9d7b4,#e6e0d2 55%,#b9c99a)" role="img" aria-label="Happy older couple smiling together"></div>
        <div class="green-bar cta" style="position:static;flex:1;margin-left:5px;padding:18px 0 0 13px">Make the most<br>from your phone mast</div>
      </div>
    </div>

    <div class="panel" style="left:277px;width:284px;background:var(--panel-grey)">
      <div class="photo sky" style="left:10px;top:15px;width:265px;height:363px;background:linear-gradient(180deg,#5e85b8,#9fb8d4 70%,#6f8a55 88%,#4c6334)" role="img" aria-label="Lattice mast topped with antennas above trees and an equipment cabin"></div>
      <h2 class="section-title abs" style="left:10px;top:398px">The current telecoms climate</h2>
      <div class="body-copy abs" style="left:10px;top:424px;width:265px">
        <p>The telecoms market, in relation to mobile phone masts, is going through some huge changes. Operators are combining to cut costs. We have already seen Trinet join forces with Tessera Mobile to form MNJV and Ozone form a jointly owned company with Voxa Telecom called CTJV. More recently, Tessera Mobile and Amberline have merged to form Allwave Networks Ltd to become the new network leader but this is set to be challenged by the take over of Ozone by Harcourt Wharton (who also own Trinet) - confused enough? Well, that’s not the end of it! Now, Britcom are hoping to buy AWN! What this can mean for the landlord is changes to their site and potentially the loss of income. It can all be very confusing but don’t worry, this is where we can help.</p>
      </div>
    </div>

    <div class="green-bar cta" style="left:282px;top:297px;width:555px;height:58px;padding:12px 0 0 28px">
      If you would like to know what rent your mast should be achieving,<br>
      check out the free rent estimation service on our website
      <svg style="width:11px;height:11px;vertical-align:-1px;margin:0 3px 0 4px" viewBox="0 0 12 12" aria-hidden="true"><circle cx="6" cy="6" r="5.3" fill="none" stroke="#fff" stroke-width="1.1"/><ellipse cx="6" cy="6" rx="2.3" ry="5.3" fill="none" stroke="#fff" stroke-width=".9"/><path d="M.7 6H11.3M1.8 3.4H10.2M1.8 8.6H10.2" stroke="#fff" stroke-width=".9"/></svg>
      www.ridgewayaerialgroup.co.uk
    </div>

    <div class="panel" style="left:561px;width:286px">
      <div class="body-copy abs" style="left:7px;top:13px;width:257px;font-size:8px">
        <p>We know the telecoms industry and understand how a new situation may affect a landlord, therefore, allowing us to provide the best advice on protecting your asset (and they are an asset despite all the hassle!)</p>
        <p>Due to all the mergers, there have been and will be more sites which become duplicates in a network and surplus to requirements. Landlords with mobile phone masts that are no longer required are receiving letters stating that the operator wishes to serve the break clause and vacate the site. In some instances, The Ridgeway Aerial Group can stop this happening. If not, we can often negotiate a substantial settlement. Phone masts which the operators wish to retain are being subjected to rent reductions. Should the reduction be refused, the operator may threaten to leave the site. All threats should be taken seriously and professional advice should be sought. There is often opportunity for negotiation. We can in most cases, prevent the rent reduction all together or significantly reduce it via our Rent Protection service.</p>
      </div>
      <p class="abs" style="left:7px;top:264px;width:260px;font-size:8.5px;line-height:12px;color:var(--ink-dark)">Landlords should not sign anything until they have sought professional advice</p>
      <h2 class="section-title abs" style="left:22px;top:371px">Our services</h2>
      <ul class="services abs" style="left:22px;top:397px">
        <li><svg viewBox="0 0 10 10"><circle cx="5" cy="5" r="4.4" fill="none" stroke="#333" stroke-width=".9"/><path d="M4 3L6 5L4 7" fill="none" stroke="#333" stroke-width="1"/></svg>Rent Reviews</li>
        <li><svg viewBox="0 0 10 10"><circle cx="5" cy="5" r="4.4" fill="none" stroke="#333" stroke-width=".9"/><path d="M4 3L6 5L4 7" fill="none" stroke="#333" stroke-width="1"/></svg>Lease Renewals</li>
        <li><svg viewBox="0 0 10 10"><circle cx="5" cy="5" r="4.4" fill="none" stroke="#333" stroke-width=".9"/><path d="M4 3L6 5L4 7" fill="none" stroke="#333" stroke-width="1"/></svg>Network Consolidation Issues</li>
        <li><svg viewBox="0 0 10 10"><circle cx="5" cy="5" r="4.4" fill="none" stroke="#333" stroke-width=".9"/><path d="M4 3L6 5L4 7" fill="none" stroke="#333" stroke-width="1"/></svg>Site Shares</li>
        <li><svg viewBox="0 0 10 10"><circle cx="5" cy="5" r="4.4" fill="none" stroke="#333" stroke-width=".9"/><path d="M4 3L6 5L4 7" fill="none" stroke="#333" stroke-width="1"/></svg>Rent Protection</li>
        <li><svg viewBox="0 0 10 10"><circle cx="5" cy="5" r="4.4" fill="none" stroke="#333" stroke-width=".9"/><path d="M4 3L6 5L4 7" fill="none" stroke="#333" stroke-width="1"/></svg>Equipment Upgrades</li>
        <li><svg viewBox="0 0 10 10"><circle cx="5" cy="5" r="4.4" fill="none" stroke="#333" stroke-width=".9"/><path d="M4 3L6 5L4 7" fill="none" stroke="#333" stroke-width="1"/></svg>Mast Removals / Decommissioning</li>
        <li><svg viewBox="0 0 10 10"><circle cx="5" cy="5" r="4.4" fill="none" stroke="#333" stroke-width=".9"/><path d="M4 3L6 5L4 7" fill="none" stroke="#333" stroke-width="1"/></svg>Mast Sales and Marketing</li>
        <li><svg viewBox="0 0 10 10"><circle cx="5" cy="5" r="4.4" fill="none" stroke="#333" stroke-width=".9"/><path d="M4 3L6 5L4 7" fill="none" stroke="#333" stroke-width="1"/></svg>Land Marketing for Masts</li>
        <li><svg viewBox="0 0 10 10"><circle cx="5" cy="5" r="4.4" fill="none" stroke="#333" stroke-width=".9"/><path d="M4 3L6 5L4 7" fill="none" stroke="#333" stroke-width="1"/></svg>Mast Management and Portfolios</li>
        <li><svg viewBox="0 0 10 10"><circle cx="5" cy="5" r="4.4" fill="none" stroke="#333" stroke-width=".9"/><path d="M4 3L6 5L4 7" fill="none" stroke="#333" stroke-width="1"/></svg>Safety Testing</li>
      </ul>
      <div class="green-bar call-bar" style="left:6px;top:561px;width:270px;height:26px">
        <span>Call us now for a free consultation!</span>
        <svg style="width:13px;height:13px;flex:none" viewBox="0 0 12 12" aria-hidden="true"><circle cx="6" cy="6" r="5.4" fill="none" stroke="#fff" stroke-width=".9"/><path d="M4 2.8L5.2 4.6L4.6 5.4Q5.4 7 6.8 7.6L7.6 7L9.3 8.2L8.6 9.3Q5.8 9.4 3.6 6.3Q2.6 4.6 3 3.4Z" fill="#fff"/></svg>
        <b>01632 960418</b>
      </div>
    </div>
  </section>

</div>
</body>
</html>
```